Stationery Design Project

We are a packaging machinery manufacturer that mainly serve the food industry.
We now require a full set of stationary including name card, envelop, letter paper, and etc. to match our company image. The logo has been awarded in a previous contest which is attached here.
Updates
Project Deadline Extended
Reason: We have extended the deadline. We have adjusted the deadline before launch to avoid confusion but it turns out the new date wasn't implemented by the system. All designers please feel free to submit your design. Thank you!
Target Market(s)
B2B customer, including decision maker in food factories, chemical factories, etc.
Industry/Entity Type
Industry
Colors
Designer to choose colors to be used in the design.
Look and feel
Each slider illustrates characteristics of the customer's brand and the style your logo design should communicate.

```html
<!DOCTYPE html>
<html lang="en">
<head>
<meta charset="utf-8">
<title>Vorane Business Cards</title>
<link rel="stylesheet" href="https://fonts.googleapis.com/css2?family=Open+Sans:wght@400;700;800&display=swap">
<style>
  :root {
    --backdrop: #939393;
    --card: #ffffff;
    --brand-green: #1f6b35;
    --text-grey: #7d8893;
    --text-white: #ffffff;
  }
  html, body {
    margin: 0;
    padding: 0;
    width: 1200px;
    height: 1200px;
    overflow: hidden;
    background: var(--backdrop);
    font-family: "Open Sans", Arial, sans-serif;
  }
  .canvas {
    position: relative;
    width: 1200px;
    height: 1200px;
  }
  .card {
    position: absolute;
    width: 700px;
    height: 400px;
    background: var(--card);
    overflow: hidden;
  }
  .card-back { left: 428px; top: 138px; }
  .card-front { left: 128px; top: 560px; }
  .chevron {
    position: absolute;
    inset: 0;
    width: 700px;
    height: 400px;
  }
  .chevron polygon { fill: var(--brand-green); }
  .phone {
    position: absolute;
    left: 61px;
    top: 254px;
    width: 260px;
    height: 28px;
    margin: 0;
    text-align: center;
    color: var(--text-white);
    font-weight: 700;
    font-size: 26px;
    letter-spacing: 1px;
    line-height: 28px;
    transform-origin: 50% 50%;
    transform: rotate(-46.8deg);
    white-space: nowrap;
  }
  .job-title {
    position: absolute;
    left: 310px;
    top: 276px;
    margin: 0;
    color: var(--text-grey);
    font-size: 23px;
    font-weight: 400;
    line-height: 1;
  }
  .person-name {
    position: absolute;
    left: 310px;
    top: 304px;
    margin: 0;
    color: var(--text-grey);
    font-size: 31px;
    font-weight: 400;
    line-height: 1;
  }
  .brand {
    position: absolute;
    left: 48px;
    top: 112px;
    display: flex;
    align-items: center;
    gap: 12px;
  }
  .brand-square {
    width: 38px;
    height: 38px;
    background: var(--brand-green);
  }
  .brand-name {
    margin: 0;
    color: var(--brand-green);
    font-weight: 800;
    font-size: 46px;
    line-height: 1;
    letter-spacing: 1px;
  }
</style>
</head>
<body>
<main class="canvas">
  <section class="card card-back" aria-label="Business card, contact side">
    <svg class="chevron" viewBox="0 0 700 400" aria-hidden="true">
      <polygon points="128,0 228,0 364,136 112,400 20,400 268,136"/>
    </svg>
    <p class="phone">(555) 210 - 4870</p>
    <p class="job-title">General Manager</p>
    <p class="person-name">Daniel Whitmore</p>
  </section>

  <section class="card card-front" aria-label="Business card, brand side">
    <svg class="chevron" viewBox="0 0 700 400" aria-hidden="true">
      <polygon points="450,0 572,0 432,138 682,400 574,400 338,138"/>
    </svg>
    <div class="brand">
      <span class="brand-square" aria-hidden="true"></span>
      <h1 class="brand-name">VORANE</h1>
    </div>
  </section>
</main>
</body>
</html>
```